Business Card Design for Kidvale (Hires out childrens play areas)

Looking to have a business card designed for a company we just bought. The company rents out childrens play areas.

I have uploaded a couple of examples of the kind of business card style I like. Here are two more examples:

https://quorvastudio.nz/project/bright-romp-branding/
https://imgvaultcdn.com/design_img/8841052/302917/302917_5518203_8841052_b73e19a2_image.jpg

I think a white card will be best due to all the colours in the logo.

Size we require: 3.75" x 2.25" (horizontally orientated) with a 0.125" bleed

Uploaded is two versions of our logo.

Details for the card:
1. My name: Liam Verster
2. Title: Managing Director
3. Phone no: 021 563 417
4. Email: liam@kidvale.co.nz
5. URL: www.kidvale.co.nz
6. Address:
PO Box 318625
Fernlea, Auckland

Let me know if you need anything else.

Target Market(s)

Hospitals, doctors surgeries, bed shops, etc.

Contact Information for Business Card

Details for the card:
1. My name: Liam Verster
3. Phone no: 021 563 417
5. URL: www.kidvale.co.nz
6. Address:
PO Box 318625
Fernlea, Auckland

Requirements
Should not have
• Not too busy.

```html
<!DOCTYPE html>
<html lang="en">
<head>
<meta charset="utf-8">
<title>Kidvale Business Card</title>
<link rel="stylesheet" href="https://fonts.googleapis.com/css2?family=Mulish:wght@400;600;700;800&display=swap">
<style>
  :root {
    --board: #ebe8e3;
    --card: #f3f3f3;
    --ink: #2b2b2b;
    --brand-blue: #1c5fb0;
    --red: #e52d2d;
    --teal: #1ba3a8;
    --orange: #f7941d;
    --green: #39b54a;
    --purple: #92278f;
  }
  * { box-sizing: border-box; margin: 0; padding: 0; }
  html, body { width: 1200px; height: 1148px; overflow: hidden; }
  body {
    background: var(--board);
    font-family: "Mulish", sans-serif;
    color: var(--ink);
    position: relative;
  }
  .card {
    position: absolute;
    background: var(--card);
    box-shadow: 3px 4px 6px rgba(0,0,0,0.35);
  }
  .card-front { left: 113px; top: 302px; width: 555px; height: 332px; }
  .card-back { left: 754px; top: 304px; width: 332px; height: 554px; }

  .wordmark {
    position: absolute;
    display: flex;
    align-items: center;
    justify-content: center;
    gap: 14px;
    color: var(--brand-blue);
    font-weight: 800;
    letter-spacing: 1px;
  }
  .wordmark-dot { border-radius: 50%; background: var(--brand-blue); flex: none; }
  .card-front .wordmark { left: 58px; top: 59px; width: 443px; height: 118px; font-size: 88px; }
  .card-front .wordmark-dot { width: 30px; height: 30px; }
  .card-back .wordmark { left: 33px; top: 70px; width: 266px; height: 170px; font-size: 64px; }
  .card-back .wordmark-dot { width: 22px; height: 22px; }

  .mascot { position: absolute; border-radius: 40%; }
  .mascot-left { left: 38px; top: 204px; width: 81px; height: 85px; background: linear-gradient(160deg, var(--teal), var(--brand-blue)); }
  .mascot-right { left: 451px; top: 223px; width: 53px; height: 81px; background: linear-gradient(180deg, var(--orange), var(--red)); }

  .address {
    position: absolute; left: 100px; top: 240px; width: 370px;
    display: flex; justify-content: center; align-items: center; gap: 12px;
    font-size: 16px; font-weight: 600;
  }
  .address .divider { width: 3px; height: 18px; background: var(--ink); }
  .web-pill {
    position: absolute; left: 200px; top: 276px; width: 175px; height: 25px;
    background: var(--brand-blue); color: #fff; border-radius: 13px;
    font-size: 14px; font-weight: 600;
    display: flex; align-items: center; justify-content: center;
  }

  .accent-band {
    position: absolute; left: 17px; width: 298px; height: 25px;
    background: linear-gradient(90deg, var(--red), var(--orange), var(--green), var(--teal), var(--brand-blue), var(--purple));
    opacity: 0.85;
  }
  .accent-band-top { top: 270px; }
  .accent-band-bottom { top: 511px; }

  .contact { position: absolute; left: 0; width: 100%; text-align: center; }
  .contact-name { top: 344px; font-size: 31px; font-weight: 400; }
  .contact-title { top: 383px; font-size: 13px; font-weight: 600; }
  .contact-phone { top: 415px; font-size: 24px; font-weight: 600; }
  .contact-email { top: 445px; font-size: 12.5px; font-weight: 600; }
</style>
</head>
<body>
  <section class="card card-front">
    <div class="wordmark"><span class="wordmark-dot"></span>Kidvale</div>
    <div class="mascot mascot-left" role="img" aria-label="Blue cartoon kid mascot tumbling"></div>
    <p class="address"><span>PO Box 318625</span><span class="divider"></span><span>Fernlea, Auckland</span></p>
    <p class="web-pill">www.kidvale.co.nz</p>
    <div class="mascot mascot-right" role="img" aria-label="Orange cartoon kid mascot jumping"></div>
  </section>

  <section class="card card-back">
    <div class="wordmark"><span class="wordmark-dot"></span>Kidvale</div>
    <div class="accent-band accent-band-top" role="img" aria-label="Decorative multicolour pattern band"></div>
    <p class="contact contact-name">Liam Verster</p>
    <p class="contact contact-title">Managing Director</p>
    <p class="contact contact-phone">021 563 417</p>
    <p class="contact contact-email">liam@kidvale.co.nz</p>
    <div class="accent-band accent-band-bottom" role="img" aria-label="Decorative multicolour pattern band"></div>
  </section>
</body>
</html>
```